Wellness Company needs 2 updated pages for our powerpoint

1 page of our powerpoint needs to be split into 2 pages. I have uploaded an image of it all on 1 page, the left side needs to be on 1 page and the right side needs to be on a separate page. I also uploaded images of the top & bottom since it is so blurry. Landscape view, please. Don't worry about the bottom of the page design since that is our template.

Target Market(s)

Wellness and Business

Industry/Entity Type

Health And Wellness

Requirements
Must have
• Clear wording and bold font.
Nice to have
• Clear circles and images

```html
<!DOCTYPE html>
<html lang="en">
<head>
<meta charset="utf-8">
<title>Compensation Plan – At a Glance</title>
<link href="https://fonts.googleapis.com/css2?family=Oswald:wght@500;600&family=Roboto:ital,wght@0,400;0,700;1,400&display=swap" rel="stylesheet">
<style>
:root{
  --stage:#d9dadc;
  --green:#7cc21d;
  --green-dark:#5fa22a;
  --green-deep:#4e9a2f;
  --orange:#f2a71b;
  --orange-pale:#fbe3a6;
  --grey:#a9a9a9;
  --grey-light:#e1e1e1;
  --ink:#3c3c3c;
  --white:#ffffff;
  --head:'Oswald',sans-serif;
  --body:'Roboto',Arial,sans-serif;
}
*{margin:0;padding:0;box-sizing:border-box}
html,body{width:1200px;height:525px;overflow:hidden}
body{background:var(--stage);position:relative;font-family:var(--body);color:var(--ink)}
.slide{position:absolute;top:87px;width:584px;height:330px;overflow:hidden;
  background:linear-gradient(180deg,#ffffff 0%,#f6faeb 55%,#e4f0c8 100%);
  box-shadow:0 6px 14px rgba(0,0,0,.25)}
.slide--one{left:12px}
.slide--two{left:604px}
.abs{position:absolute}
.brand-disc{position:absolute;left:-30px;top:-70px;width:155px;height:155px;border-radius:50%;background:var(--white);box-shadow:2px 3px 8px rgba(0,0,0,.12)}
.brand{position:absolute;left:10px;top:28px;display:flex;align-items:center;gap:5px}
.brand-dot{width:14px;height:14px;border-radius:50%;background:var(--green)}
.brand-name{font:700 12px/1.05 var(--body);color:var(--green-dark);letter-spacing:.5px}
.title-band{position:absolute;left:114px;top:14px;width:470px;height:31px;
  background:linear-gradient(90deg,var(--orange) 0%,#f6c04d 50%,var(--orange-pale) 100%);
  display:flex;align-items:center;padding-left:66px}
.title-icon{position:absolute;left:28px;top:4px}
.title-band h1{font:500 21px/1 var(--head);color:var(--white);letter-spacing:.2px}
.pill{position:absolute;height:22px;border-radius:11px;display:flex;align-items:center;justify-content:center;
  font:500 13.5px/1 var(--head);letter-spacing:.2px;z-index:3}
.pill--outline{background:var(--white);border:2.5px solid var(--green);color:var(--green-deep)}
.pill--solid{background:var(--green);color:var(--white)}
.tagline{font:700 8.3px var(--body);color:var(--orange)}
.price-list{font-size:8.3px;color:var(--green-deep)}
.price-row{position:absolute;left:205px;width:125px;display:flex;justify-content:space-between}
.price-row b{color:var(--green-deep)}
.price-rule{position:absolute;left:205px;top:122px;width:125px;border-top:1px solid var(--green)}
.keep-amount{position:absolute;left:286px;top:127px;width:36px;height:11px;border-radius:3px;background:var(--orange);color:var(--white);font:700 8px/11px var(--body);text-align:center}
.tier{position:absolute;height:19px;border-radius:3px;text-align:center;color:var(--white);font:700 6px/1 var(--body);padding-top:2px}
.tier span{display:block;font-size:8.3px;margin-top:1px}
.tier--silver{background:var(--grey)}
.tier--gold{background:var(--orange)}
.tier--platinum{background:var(--grey-light);color:#333}
.rank-badge{position:absolute;width:22px;height:22px;border-radius:50%;background:var(--green);color:var(--white);font:700 7px/22px var(--body);text-align:center}
.note-box{position:absolute;border:1.5px solid var(--green);background:var(--white);font-size:7px;line-height:1.3;padding:3px 5px 3px 12px;z-index:3}
.note-box li{margin-bottom:1px}
.note-box ul{list-style:none}
.note-box li::before{content:"●";color:var(--green);margin-left:-7px;margin-right:2px;font-size:6px}
.earn-line{font-size:8px;color:var(--green-deep)}
.dotted{position:absolute;border-top:1.2px dotted var(--green)}
.connector{position:absolute;border:1px dotted var(--orange);border-bottom:none}
.figure-slot{position:absolute;background:linear-gradient(180deg,#d8ecb6,#b9de84);border-radius:4px}
.footer-wave{position:absolute;left:0;bottom:0;z-index:1}
.site{position:absolute;left:79px;top:310px;color:var(--white);font-size:9.5px;display:flex;align-items:center;gap:5px;z-index:4}
.page-no{position:absolute;left:552px;top:304px;width:18px;height:18px;border-radius:50%;background:var(--white);border:2px solid var(--green);color:var(--green-deep);font:700 9px/14px var(--body);text-align:center;z-index:4}
/* slide two */
.chart-head{position:absolute;top:107px;font-size:8.5px;color:var(--orange);text-align:center;width:54px}
.row-no{position:absolute;left:20px;width:10px;font-size:8px;color:var(--orange);text-align:center}
.row-rule{position:absolute;left:20px;width:233px;border-top:1px solid #cfe3a8}
.bar{position:absolute;background:var(--green);color:var(--white);font-size:9px;display:flex;align-items:center;justify-content:center;border:1px solid var(--white)}
.bar--deep{background:#f5c518;color:var(--white);font-size:8px}
.unilevel-notes{position:absolute;left:20px;top:224px;font-size:7.3px;line-height:9px;color:var(--green-deep);list-style:none;z-index:3}
.unilevel-notes li::before{content:"●";margin-right:3px;font-size:6px}
.quals{position:absolute;left:292px;top:64px;width:286px;height:242px;background:linear-gradient(160deg,#6fb52b,#5ea92a);z-index:2}
.quals-list{position:absolute;left:15px;top:20px;width:266px;color:var(--white);font-size:7px;line-height:8.9px;list-style:none}
.quals-list h3{font:700 7.6px var(--body);margin-top:5px}
.quals-list p{padding-left:15px;position:relative}
.quals-list p::before{content:"●";position:absolute;left:8px;font-size:5.5px}
.quals-foot{position:absolute;right:12px;top:226px;font:italic 5.6px/7px var(--body);color:var(--white);text-align:right}
</style>
</head>
<body>

<section class="slide slide--one">
  <div class="brand-disc"></div>
  <div class="brand"><span class="brand-dot"></span><span class="brand-name">LEAFLINE<br>WELLNESS</span></div>

  <header class="title-band">
    <svg class="title-icon" width="26" height="24" viewBox="0 0 26 24" aria-hidden="true">
      <circle cx="14" cy="8" r="7" fill="#fff"/>
      <text x="14" y="11.5" text-anchor="middle" font-family="Roboto,Arial,sans-serif" font-weight="700" font-size="10" fill="#f2a71b">$</text>
      <path d="M1 19 Q7 14 13 17 L20 16 Q24 15 25 17 L16 22 L4 22 Z" fill="#fff"/>
    </svg>
    <h1>COMPENSATION PLAN - AT A GLANCE</h1>
  </header>

  <div class="pill pill--outline" style="left:186px;top:54px;width:163px">1. DIRECT SELLING</div>
  <p class="abs tagline" style="left:205px;top:81px">Sell the product. Keep the profit.</p>
  <div class="price-list">
    <div class="price-row" style="top:99px"><span>● Suggested Retail</span><b>$34.95</b></div>
    <div class="price-row" style="top:109px"><span>● Wholesale</span><b>$24.95</b></div>
    <div class="price-rule"></div>
    <div class="price-row" style="top:127px;color:var(--orange)"><span>●You Keep</span></div>
    <div class="keep-amount">$10.00</div>
  </div>

  <div class="pill pill--outline" style="left:396px;top:54px;width:163px">2. FAST START BONUS</div>
  <div class="figure-slot" role="img" aria-label="Icon of a business person with coins" style="left:462px;top:80px;width:29px;height:28px"></div>
  <div class="connector" style="left:418px;top:102px;width:119px;height:11px"></div>
  <div class="tier tier--silver" style="left:396px;top:113px;width:44px">Silver<span>$10.00</span></div>
  <div class="tier tier--gold" style="left:452px;top:113px;width:49px">Gold<span>$20.00</span></div>
  <div class="tier tier--platinum" style="left:509px;top:113px;width:50px">Platinum<span>$40.00</span></div>
  <p class="abs earn-line" style="left:396px;top:136px;width:163px;text-align:center">Earn <b>up to $40</b> for each Package you sell</p>

  <div class="pill pill--solid" style="left:6px;top:140px;width:165px">3. LEADERSHIP BONUS</div>
  <div class="dotted" style="left:171px;top:152px;width:401px"></div>

  <div class="connector" style="left:47px;top:184px;width:117px;height:9px"></div>
  <div class="rank-badge" style="left:91px;top:164px">MBO</div>
  <div class="tier tier--silver" style="left:22px;top:193px;width:50px">Silver<span>$10.00</span></div>
  <div class="tier tier--gold" style="left:79px;top:193px;width:50px">Gold<span>$20.00</span></div>
  <div class="tier tier--platinum" style="left:136px;top:193px;width:50px">Platinum<span>$40.00</span></div>
  <ul class="note-box" style="left:22px;top:219px;width:164px;height:25px">
    <li>MBO's earn up to <b>$10, $20, or $40</b> per enrollment package sold.</li>
  </ul>

  <div class="connector" style="left:235px;top:184px;width:117px;height:9px"></div>
  <div class="rank-badge" style="left:282px;top:164px">SBO</div>
  <div class="tier tier--silver" style="left:210px;top:193px;width:50px">Silver<span>$20.00</span></div>
  <div class="tier tier--gold" style="left:267px;top:193px;width:50px">Gold<span>$40.00</span></div>
  <div class="tier tier--platinum" style="left:323px;top:193px;width:51px">Platinum<span>$80.00</span></div>
  <ul class="note-box" style="left:210px;top:219px;width:164px;height:50px">
    <li>SBO's earn up to <b>$20, $40, or $80</b> per enrollment package sold.</li>
    <li>SBO leadership bonus may be split between different leaders. MBOs and SBOs will split the difference between bonuses.</li>
  </ul>

  <div class="connector" style="left:426px;top:184px;width:117px;height:9px"></div>
  <div class="rank-badge" style="left:475px;top:164px">EBO</div>
  <div class="tier tier--silver" style="left:401px;top:193px;width:50px">Silver<span>$40.00</span></div>
  <div class="tier tier--gold" style="left:458px;top:193px;width:50px">Gold<span>$80.00</span></div>
  <div class="tier tier--platinum" style="left:515px;top:193px;width:50px">Platinum<span>$160.00</span></div>
  <ul class="note-box" style="left:400px;top:219px;width:165px;height:50px">
    <li>EBO's earn up to <b>$40, $80, or $160</b> per enrollment package sold.</li>
    <li>SBO leadership bonus may be split between different leaders. EBOs, MBOs and SBOs will split the difference between bonuses.</li>
  </ul>

  <svg class="footer-wave" width="584" height="72" viewBox="0 0 584 72" aria-hidden="true">
    <path d="M0 34 C120 0 300 6 470 44 L584 58 L584 72 L0 72 Z" fill="#f2a71b"/>
    <path d="M0 56 C180 40 380 62 584 30 L584 72 L0 72 Z" fill="#5fa22a"/>
    <path d="M320 20 C420 40 500 48 584 40" stroke="#7cc21d" stroke-width="2" fill="none"/>
  </svg>
  <div class="site">
    <svg width="11" height="11" viewBox="0 0 12 12" aria-hidden="true"><circle cx="6" cy="6" r="5" fill="none" stroke="#fff" stroke-width="1.2"/><path d="M1 6h10M6 1c-3 3-3 7 0 10M6 1c3 3 3 7 0 10" stroke="#fff" fill="none"/></svg>
    www.leaflinewellness.com
  </div>
  <div class="page-no">1</div>
</section>

<section class="slide slide--two">
  <div class="brand-disc"></div>
  <div class="brand"><span class="brand-dot"></span><span class="brand-name">LEAFLINE<br>WELLNESS</span></div>

  <header class="title-band">
    <svg class="title-icon" width="26" height="24" viewBox="0 0 26 24" aria-hidden="true">
      <circle cx="14" cy="8" r="7" fill="#fff"/>
      <text x="14" y="11.5" text-anchor="middle" font-family="Roboto,Arial,sans-serif" font-weight="700" font-size="10" fill="#f2a71b">$</text>
      <path d="M1 19 Q7 14 13 17 L20 16 Q24 15 25 17 L16 22 L4 22 Z" fill="#fff"/>
    </svg>
    <h1>COMPENSATION PLAN - AT A GLANCE</h1>
  </header>

  <div class="pill pill--solid" style="left:124px;top:52px;width:164px">4. UNILEVEL COMMISSION</div>

  <div class="quals">
    <ul class="quals-list">
      <li><h3>1. INDEPENDENT BUSINESS OWNER (IBO)</h3>
        <p>Enroll as an Active Independent Business Owner</p>
        <p>After your first month to remain active you must personally maintain a minimum of <b>25</b> business volume &amp; subscribe to autoship</p></li>
      <li><h3>2. MANAGING BUSINESS OWNER (MBO)</h3>
        <p>Be an Active IBO and personaly maintain <b>50</b> business volume</p>
        <p>Personally sponsor <b>3 IBO's</b>. Each of them must be active</p></li>
      <li><h3>3. SENIOR BUSINESS OWNER (SBO)</h3>
        <p>Be an Active IBO and personaly maintain <b>100</b> business volume</p>
        <p>Promote <b>3 MBO's</b> in 3 Separate Legs</p>
        <p>Maintain <b>1500</b> combined business volume for entire downline</p></li>
      <li><h3>4. EXECUTIVE BUSINESS OWNER (EBO)</h3>
        <p>Be an Active IBO and personaly maintain <b>200</b> business volume</p>
        <p>Promote <b>3 SBO's</b> in 3 Separate Legs</p>
        <p>Maintain <b>5000</b> combined business volume for entire downline</p></li>
      <li><h3>5. REGIONAL EXECUTIVE BUSINESS OWNER (REBO)</h3>
        <p>Be an Active IBO and personaly maintain <b>400</b> business volume</p>
        <p>Promote <b>3 EBO's</b> in 3 Separate Legs</p>
        <p>Maintain <b>15000</b> combined business volume for entire downline</p></li>
    </ul>
    <p class="quals-foot">* All requirements must be met to stay commissionable within the rank.<br>This is an example only, see full commission plan for details.</p>
  </div>
  <div class="pill pill--solid" style="left:298px;top:52px;width:165px;border:2px solid #fff">
    <svg width="12" height="12" viewBox="0 0 24 24" aria-hidden="true"><path d="M12 1l3.3 7 7.7.9-5.7 5.2 1.6 7.6L12 18l-6.9 3.7 1.6-7.6L1 8.9 8.7 8z" fill="#fff"/></svg>
    &nbsp;QUALIFICATIONS&nbsp;
    <svg width="12" height="12" viewBox="0 0 24 24" aria-hidden="true"><path d="M12 1l3.3 7 7.7.9-5.7 5.2 1.6 7.6L12 18l-6.9 3.7 1.6-7.6L1 8.9 8.7 8z" fill="#fff"/></svg>
  </div>

  <div class="chart-head" style="left:31px">IBO</div>
  <div class="chart-head" style="left:86px">MBO</div>
  <div class="chart-head" style="left:140px">SBO</div>
  <div class="chart-head" style="left:195px">EBO/REBO</div>

  <div class="row-no" style="top:121px">1</div><div class="row-rule" style="top:133px"></div>
  <div class="row-no" style="top:133px">2</div><div class="row-rule" style="top:145px"></div>
  <div class="row-no" style="top:145px">3</div><div class="row-rule" style="top:157px"></div>
  <div class="row-no" style="top:157px">4</div><div class="row-rule" style="top:169px"></div>
  <div class="row-no" style="top:169px">5</div><div class="row-rule" style="top:181px"></div>
  <div class="row-no" style="top:181px">6</div><div class="row-rule" style="top:193px"></div>
  <div class="row-no" style="top:193px">7</div><div class="row-rule" style="top:205px"></div>
  <div class="row-no" style="top:205px">8</div><div class="row-rule" style="top:217px"></div>

  <div class="bar" style="left:32px;top:121px;width:54px;height:24px">5%</div>
  <div class="bar" style="left:86px;top:121px;width:54px;height:48px">5%</div>
  <div class="bar" style="left:140px;top:121px;width:55px;height:72px">5%</div>
  <div class="bar" style="left:195px;top:121px;width:54px;height:84px">5%</div>
  <div class="bar bar--deep" style="left:195px;top:205px;width:54px;height:12px">10%</div>

  <ul class="unilevel-notes">
    <li><b>IBOs</b> earn 5% commission on all sales <b>2</b> levels deep</li>
    <li><b>MBOs</b> earn 5% commission on all sales <b>4</b> levels deep</li>
    <li><b>SBOs</b> earn 5% commission on all sales <b>6</b> levels deep</li>
    <li><b>EBOs</b> earn 5% commission on all sales <b>7</b> levels deep and 10% on the <b>8th</b> level</li>
  </ul>

  <svg class="footer-wave" width="584" height="72" viewBox="0 0 584 72" aria-hidden="true">
    <path d="M0 34 C120 0 300 6 470 44 L584 58 L584 72 L0 72 Z" fill="#f2a71b"/>
    <path d="M0 56 C180 40 380 62 584 30 L584 72 L0 72 Z" fill="#5fa22a"/>
    <path d="M320 20 C420 40 500 48 584 40" stroke="#7cc21d" stroke-width="2" fill="none"/>
  </svg>
  <div class="site" style="left:77px">
    <svg width="11" height="11" viewBox="0 0 12 12" aria-hidden="true"><circle cx="6" cy="6" r="5" fill="none" stroke="#fff" stroke-width="1.2"/><path d="M1 6h10M6 1c-3 3-3 7 0 10M6 1c3 3 3 7 0 10" stroke="#fff" fill="none"/></svg>
    www.leaflinewellness.com
  </div>
  <div class="page-no">2</div>
</section>

</body>
</html>
```